TRIVAN 2026 Flyer for Conference

TRIVAN needs a design for a 1-page flyer that we will hand out at an upcoming event & then later post online as a pdf. There are 3 elements which need to be on the flyer:

1) A logo. This should be prominent on the design (e.g., in the middle). The flyer should use the colors that are in that logo (e.g., for accents, design elements, and/or text; not all of these have to be used):
Dark blue: #185577
Med blue: #327C9A
Teal: #4EB1C2
Light Teal: #9EDBE6

2) The conference theme -- Forests of Wonder: Climbing toward Research Fluency -- should be at the flyer's top.

3) Finally, these six tracks should be listed below the theme and the logo (it's font size should be at least a couple sizes smaller than the size used for the theme):
- Pearls of Pedagogy: Teaching Techniques that Work
- The Depth Gauge: Measuring Instructional Impact
- Techtonic Shifts: Innovation and Educational Technology
- Captain's Log: Navigating Leadership in Library Instruction
- Swimming Together: Collaborating with Others
- The Bermuda Triangle: Exploring (Seemingly) Eternal Challenges

Font styles to use
Sans Serif

Colors
0094D4
00A9DD
6FCCEA
C7EBF8
E9F6FB

Requirements
Must have
• The 3 elements listed in the description: 1) the logo, 2) the text of the theme and 3) the text for the tracks.

```html
<!DOCTYPE html>
<html lang="en">
<head>
<meta charset="utf-8">
<title>TRIVAN 2026 – Forests of Wonder</title>
<link href="https://fonts.googleapis.com/css2?family=Montserrat:wght@500;600;700&display=swap" rel="stylesheet">
<style>
  :root {
    --navy: #1c5578;
    --navy-deep: #1d5577;
    --teal: #4eb1c2;
    --teal-light: #9edbe6;
    --sky: #cdeaf8;
    --white: #ffffff;
    --ink: #1b1b1b;
  }
  * { margin: 0; padding: 0; box-sizing: border-box; }
  html, body { width: 891px; height: 1200px; overflow: hidden; background: var(--white); }
  .flyer {
    position: relative; width: 891px; height: 1200px; overflow: hidden;
    font-family: "Montserrat", sans-serif;
    background: linear-gradient(180deg, var(--sky) 0%, #e6f5fc 16%, var(--white) 30%);
  }
  .band-shape { position: absolute; left: 0; top: 0; width: 891px; height: 1200px; }
  .theme-title {
    position: absolute; left: 62px; top: 58px;
    color: var(--navy); font-weight: 700; font-size: 64px; line-height: 62px; letter-spacing: 0.5px;
  }
  .theme-subtitle {
    position: absolute; left: 62px; top: 262px;
    color: var(--teal); font-weight: 600; font-size: 36px; line-height: 38px;
  }
  .brand {
    position: absolute; left: 600px; top: 96px;
    display: flex; align-items: center; gap: 10px;
    color: var(--navy); font-weight: 700; font-size: 30px;
  }
  .brand-dot { width: 26px; height: 26px; border-radius: 50%; background: var(--teal); }
  .photo {
    position: absolute; left: 551px; top: 228px; width: 269px; height: 972px;
    border-radius: 134.5px 134.5px 0 0;
    background: linear-gradient(180deg, #6b5a48 0%, #c89a62 18%, #d9b98e 40%, #bfc9c8 62%, #8fc7cf 80%, var(--teal) 100%);
  }
  .tracks { position: absolute; left: 0; top: 397px; list-style: none; }
  .track { position: absolute; left: 0; width: 540px; height: 90px; }
  .track-pin { position: absolute; left: 29px; top: 2px; width: 34px; height: 48px; }
  .track-name { position: absolute; left: 107px; top: 0; font-weight: 700; font-size: 22px; color: var(--navy); white-space: nowrap; }
  .track-desc { position: absolute; left: 107px; top: 31px; font-weight: 500; font-size: 15.5px; color: var(--ink); white-space: nowrap; }
  .track.on-dark .track-name, .track.on-dark .track-desc { color: var(--white); }
  .dates-frame {
    position: absolute; left: 30px; top: 989px; width: 250px; height: 120px;
    border-left: 3px solid var(--teal); border-top: 3px solid var(--teal); border-top-width: 3px;
  }
  .dates-frame::after { content: none; }
  .dates-lead { position: absolute; left: 130px; top: 1000px; }
  .classes { position: absolute; left: 130px; }
  .dates-block { position: absolute; left: 43px; top: 998px; }
  .dates-label { color: var(--teal); font-weight: 700; font-size: 29px; line-height: 34px; white-space: nowrap; }
  .dates-range { color: var(--white); font-weight: 700; font-size: 30px; line-height: 40px; }
  .dates-venue { color: var(--white); font-weight: 700; font-size: 16px; line-height: 26px; }
  .site { position: absolute; left: 43px; top: 1141px; color: var(--white); font-weight: 600; font-size: 14.5px; }
</style>
</head>
<body>
<div class="flyer">
  <svg class="band-shape" viewBox="0 0 891 1200" aria-hidden="true">
    <path d="M0 668 H551 V1200 H0 Z" fill="#1d5577"/>
    <path d="M820 733 C862 760 891 815 891 880 V1200 H820 Z" fill="#1d5577"/>
  </svg>

  <h1 class="theme-title">FORESTS OF<br>WONDER</h1>
  <p class="theme-subtitle">CLIMBING TOWARD<br>RESEARCH<br>FLUENCY</p>

  <div class="brand"><span class="brand-dot"></span><span>TRIVAN 2026</span></div>

  <div class="photo" role="img" aria-label="Photo of a student browsing tall wooden library bookshelves"></div>

  <ol class="tracks">
    <li class="track" style="top:0">
      <svg class="track-pin" viewBox="0 0 34 48"><path d="M17 1 A16 16 0 0 1 17 33 A16 16 0 0 1 17 1 Z" fill="#9edbe6"/><circle cx="17" cy="17" r="16" fill="#6fc2d2"/><path d="M11 31 L17 42 L23 31 Z" fill="#4eb1c2"/><circle cx="17" cy="17" r="12" fill="#fff"/><text x="17" y="22" text-anchor="middle" font-family="Montserrat, sans-serif" font-weight="700" font-size="13" fill="#1c5578">01</text></svg>
      <span class="track-name">Pearls Of Pedagogy</span><span class="track-desc">Teaching Techniques that Work</span>
    </li>
    <li class="track" style="top:103px">
      <svg class="track-pin" viewBox="0 0 34 48"><circle cx="17" cy="17" r="16" fill="#6fc2d2"/><path d="M11 31 L17 42 L23 31 Z" fill="#4eb1c2"/><circle cx="17" cy="17" r="12" fill="#fff"/><text x="17" y="22" text-anchor="middle" font-family="Montserrat, sans-serif" font-weight="700" font-size="13" fill="#1c5578">02</text></svg>
      <span class="track-name">The Depth Gauge</span><span class="track-desc">Measuring Instructional Impact</span>
    </li>
    <li class="track" style="top:203px">
      <svg class="track-pin" viewBox="0 0 34 48"><circle cx="17" cy="17" r="16" fill="#6fc2d2"/><path d="M11 31 L17 42 L23 31 Z" fill="#4eb1c2"/><circle cx="17" cy="17" r="12" fill="#fff"/><text x="17" y="22" text-anchor="middle" font-family="Montserrat, sans-serif" font-weight="700" font-size="13" fill="#1c5578">03</text></svg>
      <span class="track-name">Techtonic Shifts</span><span class="track-desc">Innovation and Educational Technology</span>
    </li>
    <li class="track on-dark" style="top:302px">
      <svg class="track-pin" viewBox="0 0 34 48"><circle cx="17" cy="17" r="16" fill="#6fc2d2"/><path d="M11 31 L17 42 L23 31 Z" fill="#4eb1c2"/><circle cx="17" cy="17" r="12" fill="#fff"/><text x="17" y="22" text-anchor="middle" font-family="Montserrat, sans-serif" font-weight="700" font-size="13" fill="#1c5578">04</text></svg>
      <span class="track-name">Captain's Log</span><span class="track-desc">Navigating Leadership in Library Instruction</span>
    </li>
    <li class="track on-dark" style="top:402px">
      <svg class="track-pin" viewBox="0 0 34 48"><circle cx="17" cy="17" r="16" fill="#6fc2d2"/><path d="M11 31 L17 42 L23 31 Z" fill="#4eb1c2"/><circle cx="17" cy="17" r="12" fill="#fff"/><text x="17" y="22" text-anchor="middle" font-family="Montserrat, sans-serif" font-weight="700" font-size="13" fill="#1c5578">05</text></svg>
      <span class="track-name">Swimming Together</span><span class="track-desc">Collaborating with Others</span>
    </li>
    <li class="track on-dark" style="top:501px">
      <svg class="track-pin" viewBox="0 0 34 48"><circle cx="17" cy="17" r="16" fill="#6fc2d2"/><path d="M11 31 L17 42 L23 31 Z" fill="#4eb1c2"/><circle cx="17" cy="17" r="12" fill="#fff"/><text x="17" y="22" text-anchor="middle" font-family="Montserrat, sans-serif" font-weight="700" font-size="13" fill="#1c5578">06</text></svg>
      <span class="track-name">The Bermuda Triangle</span><span class="track-desc">Exploring (Seemingly) Eternal Challenges</span>
    </li>
  </ol>

  <div class="dates-frame"></div>
  <div class="dates-block">
    <p class="dates-label">CLASSES STARTING</p>
    <p class="dates-range">MAY 7-9</p>
    <p class="dates-venue">TRIVAN Ashgrove, VA</p>
  </div>
  <p class="site">www.trivanashgrove.com</p>
</div>
</body>
</html>
```